Natural Skincare brand needs new labels!

We are a natural and organic skin care brand based in the united states. We are looking for unique product label designs that will help our brand stand out. We want the labels to look elegant and natural, but also incorporate some color. We want a design aspect like a line drawing on the labels, see examples. Please refer to our website to see our current labels and to get more of a feel of who we are. Our logo is included. We are looking for 5 labels for 5 different Products.
1. Body butter: 1.5"x9" rectangle wrap around 12oz jar with black lid
2. Eczema Salve: 1.5" circle silver metal tin
3. Glow Serum: 1.5"x3" rectangle Blue Dropper Bottle with black top
4. Mineral Mist: 1.5"x3" clear glass sprayer bottle (want clear label)
website: www.velmirabotanics.com
Instagram: @velmirabotanics

```html
<!DOCTYPE html>
<html lang="en">
<head>
<meta charset="utf-8">
<title>Velmira Botanics — Skincare Labels</title>
<link rel="stylesheet" href="https://fonts.googleapis.com/css2?family=Poppins:ital,wght@0,400;0,500;0,600;1,600&family=Hind:wght@400;500&display=swap">
<style>
  :root {
    --canvas: #ebe8e6;
    --label: #f4f4f4;
    --lid-label: #e9e9e9;
    --ink: #262626;
    --coral: #dd7566;
    --coral-soft: #f08a7b;
    --lavender: #8f7cc4;
    --lavender-soft: #a593d3;
    --dash: #7d7d7d;
    --line-art: #c9c6c6;
    --white: #ffffff;
  }
  * { box-sizing: border-box; margin: 0; padding: 0; }
  html, body { width: 1170px; height: 1200px; overflow: hidden; }
  body {
    position: relative;
    background: var(--canvas);
    font-family: "Poppins", sans-serif;
    color: var(--ink);
  }

  /* ---------- Shared brand lockup ---------- */
  .brand { position: absolute; display: flex; align-items: center; }
  .brand-name {
    font-family: "Poppins", sans-serif;
    font-weight: 500;
    color: var(--coral);
    line-height: 1;
    white-space: nowrap;
  }
  .brand-dot { border-radius: 50%; background: var(--coral); flex: none; }

  /* ---------- Round salve label ---------- */
  .salve-label {
    position: absolute;
    left: 285px; top: 110px;
    width: 600px; height: 600px;
    border-radius: 50%;
    background: var(--lid-label);
    border: 8px solid var(--lavender);
    overflow: hidden;
  }
  .salve-label .brand { left: 96px; top: 112px; gap: 10px; }
  .salve-label .brand-name { font-size: 80px; letter-spacing: -1px; }
  .salve-label .brand-dot { width: 34px; height: 34px; margin-top: -40px; }
  .product-title {
    position: absolute; left: 94px; top: 286px;
    font-family: "Hind", sans-serif; font-weight: 500;
    font-size: 36px; line-height: 1; white-space: nowrap;
  }
  .benefit-tag {
    position: absolute; left: 96px; top: 324px;
    background: var(--coral); color: var(--white);
    font-family: "Hind", sans-serif; font-weight: 500;
    font-size: 18px; line-height: 1; padding: 5px 6px 2px;
    white-space: nowrap;
  }
  .natural-note {
    position: absolute; left: 95px; top: 366px;
    font-size: 14px; font-weight: 400; white-space: nowrap;
  }
  .ingredient-list {
    position: absolute; left: 96px; top: 405px;
    font-size: 15px; line-height: 20px; font-weight: 400; white-space: nowrap;
  }
  .net-weight {
    position: absolute; left: 214px; top: 522px;
    font-size: 24px; font-weight: 400; line-height: 1;
  }
  .salve-label .size-tab {
    position: absolute; left: 280px; top: 512px;
    width: 48px; height: 90px;
    background: var(--lavender); color: var(--white);
    border-radius: 24px 24px 0 0;
    font-size: 20px; text-align: center; padding-top: 8px; line-height: 1.2;
  }
  .salve-label .size-tab sup { font-size: 12px; }
  .salve-label .line-art {
    position: absolute; left: 380px; top: 210px;
    width: 180px; height: 330px;
    border-radius: 40px;
    background: linear-gradient(160deg, var(--line-art), var(--lid-label));
  }

  /* ---------- Wrap-around body butter label ---------- */
  .wrap-label {
    position: absolute; left: 40px; top: 800px;
    width: 1090px; height: 182px;
    background: var(--label);
    border-top: 7px solid var(--lavender-soft);
    border-bottom: 3px solid var(--coral-soft);
    box-shadow: 0 3px 5px rgba(0,0,0,0.25);
  }
  .wrap-label .scallop {
    position: absolute; left: 0; top: 0; width: 100%; height: 5px;
    background: radial-gradient(circle at 4px 0, var(--lavender-soft) 4px, transparent 4.5px);
    background-size: 8px 5px;
  }
  .panel-copy {
    position: absolute; font-size: 6.3px; line-height: 7.2px;
    text-align: justify; font-weight: 400;
  }
  .panel-copy b { font-weight: 600; font-size: 6.8px; }
  .ingredients-copy { left: 32px; top: 27px; width: 296px; }
  .usage-copy { left: 758px; top: 27px; width: 296px; }
  .care-copy { left: 758px; top: 88px; width: 296px; }
  .caution-box {
    position: absolute; left: 32px; top: 102px;
    width: 296px; height: 48px;
    border: 1.5px dashed var(--dash); border-radius: 24px;
    padding: 6px 16px;
    font-size: 6.2px; line-height: 8px; font-style: italic; font-weight: 600;
    color: var(--coral-soft); text-align: justify;
  }
  .natural-pill {
    position: absolute; left: 760px; top: 136px;
    width: 200px; height: 22px; border-radius: 11px;
    background: var(--coral-soft); color: var(--white);
    font-size: 9.5px; font-weight: 600; white-space: nowrap;
    display: flex; align-items: center; padding-left: 9px;
  }
  .wrap-label .line-art {
    position: absolute; left: 388px; top: 9px;
    width: 150px; height: 138px; border-radius: 30px;
    background: linear-gradient(150deg, var(--line-art), var(--label));
  }
  .wrap-label .brand { left: 570px; top: 38px; gap: 5px; }
  .wrap-label .brand-name { font-size: 32px; letter-spacing: -0.5px; }
  .wrap-label .brand-dot { width: 13px; height: 13px; margin-top: -16px; }
  .butter-title {
    position: absolute; left: 560px; top: 88px;
    font-family: "Hind", sans-serif; font-weight: 500;
    font-size: 20px; line-height: 1; white-space: nowrap;
  }
  .butter-title .accent { color: var(--coral-soft); }
  .scent-band {
    position: absolute; left: 563px; top: 111px;
    width: 122px; height: 16px;
    background: var(--lavender-soft); color: var(--white);
    font-size: 9.5px; letter-spacing: 6px; text-align: center; line-height: 17px;
    padding-left: 6px;
  }
  .skin-note {
    position: absolute; left: 561px; top: 133px;
    font-family: "Hind", sans-serif; font-size: 7px; line-height: 9px;
  }
  .wrap-label .size-tab {
    position: absolute; left: 663px; top: 154px; width: 26px; height: 18px;
    background: var(--coral-soft); color: var(--white);
    border-radius: 13px 13px 0 0; text-align: center;
    font-size: 8px; padding-top: 4px; line-height: 1.2;
  }
  .wrap-label .size-tab sup { font-size: 5px; }
</style>
</head>
<body>

  <section class="salve-label" aria-label="Eczema salve lid label">
    <div class="brand">
      <span class="brand-name">Velmira</span>
      <span class="brand-dot"></span>
    </div>
    <h1 class="product-title">ECZEMA SALVE</h1>
    <div class="benefit-tag">HEALING &amp; REGENERATING</div>
    <p class="natural-note">Made With all natural ingredients</p>
    <p class="ingredient-list">sesame oil^, calendula flow-<br>ers^, licorice root^, plantain<br>leaf^, vitamin E oil^, beeswax^</p>
    <span class="net-weight">29g</span>
    <div class="size-tab">1<sup>OZ</sup></div>
    <div class="line-art" role="img" aria-label="Line drawing of a flowering stem with leaves"></div>
  </section>

  <section class="wrap-label" aria-label="Lavender body butter wrap label">
    <div class="scallop"></div>

    <p class="panel-copy ingredients-copy"><b>Ingredients</b> Shea butter, cocoa butter, mango butter, sweet almond oil, jojoba oil, coconut oil, lavender essential oil, vitamin E oil and beeswax, blended in small batches to soften, soothe and protect dry, tender skin. Free from parabens, sulfates, dyes and synthetic fragrance. For external use only. Store in a cool, dry place away from direct sunlight. Keep lid closed tightly after each use. Avoid contact with eyes. Keep out of reach of children. Discontinue use if redness or irritation develops and consult a doctor.</p>
    <p class="caution-box">Gentle enough for daily use on sensitive skin. Patch test before first use and stop use if irritation occurs. Handmade with care in small batches from plant butters and pure oils, never tested on animals.</p>

    <div class="line-art" role="img" aria-label="Line drawing of a leafy lavender sprig"></div>

    <div class="brand">
      <span class="brand-name">Velmira</span>
      <span class="brand-dot"></span>
    </div>
    <h2 class="butter-title">BODY <span class="accent">BUTTER</span></h2>
    <div class="scent-band">LAVENDER</div>
    <p class="skin-note">Mouisturizing+Nourishing+Sensitive<br>Dry Skin</p>
    <div class="size-tab">12<sup>OZ</sup></div>

    <p class="panel-copy usage-copy"><b>How to use</b> Scoop a small amount with clean, dry fingers and warm it between your palms. Massage into damp skin after bathing, focusing on elbows, knees, heels and any dry patches. Use morning and night, or as often as needed. A little goes a long way, so start small and add more as your skin drinks it in. Lavender calms the senses, making it a lovely ritual before bed. Follow with your favourite oil for extra softness.</p>
    <p class="panel-copy care-copy">Our butters are whipped by hand and may soften in warm weather. If it melts, simply chill it and the texture returns. Each jar is poured fresh, so slight changes in colour and scent are natural. Recycle the jar when empty.</p>
    <div class="natural-pill">Made With all natural ingredients</div>
  </section>

</body>
</html>
```